business card design for luxurious real estate brand

using the attached logo, i am looking for a 2-sided business card design. the back should be the gold logo on black background. the front needs to include: gold logo, name, phone, email, and website

Industry/Entity Type

real estate

Contact Information for Business Card

logo, name, email, phone, website

Font styles to use
Sans Serif

```html
<!DOCTYPE html>
<html lang="en">
<head>
<meta charset="utf-8">
<title>Casa Ridgeway — Business Card</title>
<link href="https://fonts.googleapis.com/css2?family=Open+Sans:wght@400;700&display=swap" rel="stylesheet">
<style>
  :root {
    --backdrop: #d6d6d6;
    --card-black: #1a1a1a;
    --pattern-light: #2e2e2e;
    --pattern-dark: #0d0d0d;
    --gold: #ffcc00;
    --ink-light: #f2f2f2;
  }
  * { margin: 0; padding: 0; box-sizing: border-box; }
  html, body {
    width: 1200px; height: 896px; overflow: hidden;
    background: var(--backdrop);
    font-family: "Open Sans", sans-serif;
  }
  .canvas { position: relative; width: 1200px; height: 896px; }
  .card {
    position: absolute; left: 334px; width: 528px; height: 300px;
    border-radius: 26px; overflow: hidden;
    background: var(--card-black);
    box-shadow: 0 14px 24px rgba(0,0,0,0.25);
  }
  .card--back { top: 126px; }
  .card--front { top: 475px; }

  .back-pattern {
    position: absolute; inset: 0;
    background: linear-gradient(115deg, var(--pattern-light) 0%, #1f1f1f 50%, var(--pattern-dark) 100%);
  }
  .back-brand {
    position: absolute; right: 20px; top: 218px;
    display: flex; align-items: center; gap: 10px;
    color: var(--gold); font-weight: 700; font-size: 17px; letter-spacing: 4px;
  }
  .brand-dot { width: 14px; height: 14px; border-radius: 50%; background: var(--gold); }

  .front-brand {
    position: absolute; left: 0; right: 0; top: 58px;
    display: flex; flex-direction: column; align-items: center; gap: 22px;
  }
  .front-brand .brand-mark { width: 34px; height: 34px; border-radius: 50%; background: var(--gold); }
  .front-brand .brand-name {
    color: var(--gold); font-weight: 700; font-size: 24px; letter-spacing: 6px;
  }

  .holder {
    position: absolute; right: 292px; top: 214px; text-align: right;
  }
  .holder-name { color: var(--gold); font-weight: 700; font-size: 20px; line-height: 24px; }
  .holder-title { color: var(--ink-light); font-size: 13px; line-height: 20px; }

  .divider {
    position: absolute; left: 253px; top: 217px; width: 1.5px; height: 53px;
    background: var(--gold);
  }
  .contacts {
    position: absolute; left: 268px; top: 212px; list-style: none;
    color: var(--ink-light); font-size: 13px; line-height: 20px;
  }
  .contacts li { display: flex; align-items: center; gap: 6px; }
  .contacts svg { width: 11px; height: 11px; fill: var(--gold); flex: none; }

  .footer-band { position: absolute; left: 0; bottom: 0; width: 528px; height: 15px; }
</style>
</head>
<body>
<main class="canvas">

  <section class="card card--back" aria-label="Card back">
    <div class="back-pattern" role="img" aria-label="Tonal repeating brand pattern in dark greys"></div>
    <div class="back-brand">
      <span class="brand-dot"></span>
      <span class="brand-name">CASA RIDGEWAY</span>
    </div>
  </section>

  <section class="card card--front" aria-label="Card front">
    <div class="front-brand">
      <span class="brand-mark"></span>
      <span class="brand-name">CASA RIDGEWAY</span>
    </div>

    <div class="holder">
      <p class="holder-name">MARTIN HALE</p>
      <p class="holder-title">Managing Director</p>
    </div>

    <div class="divider"></div>

    <ul class="contacts">
      <li>
        <svg viewBox="0 0 24 24"><path d="M6.6 10.8a15.1 15.1 0 0 0 6.6 6.6l2.2-2.2c.3-.3.7-.4 1-.2 1.1.4 2.3.6 3.6.6.6 0 1 .4 1 1V20c0 .6-.4 1-1 1A17 17 0 0 1 3 4c0-.6.4-1 1-1h3.5c.6 0 1 .4 1 1 0 1.3.2 2.5.6 3.6.1.3 0 .7-.2 1z"/></svg>
        555 014 272
      </li>
      <li>
        <svg viewBox="0 0 24 24"><path d="M2 5h20v2l-10 6L2 7z"/><path d="M2 9.3l10 6 10-6V19H2z"/></svg>
        hello@casaridgeway.com
      </li>
      <li>
        <svg viewBox="0 0 24 24"><path d="M12 2a10 10 0 1 0 0 20 10 10 0 0 0 0-20zm-1 17.9A8 8 0 0 1 4.1 9.9L9 15v1a2 2 0 0 0 2 2zm6.9-2.5A2 2 0 0 0 16 16h-1v-3a1 1 0 0 0-1-1H8v-2h2a1 1 0 0 0 1-1V7h2a2 2 0 0 0 2-2v-.4a8 8 0 0 1 2.9 12.8z"/></svg>
        www.casaridgeway.com
      </li>
    </ul>

    <svg class="footer-band" viewBox="0 0 528 15" aria-hidden="true">
      <polygon points="0,4 248,4 240,15 0,15" fill="var(--gold)"/>
      <polygon points="262,4 528,4 528,15 251,15" fill="var(--gold)"/>
    </svg>
  </section>

</main>
</body>
</html>
```